Business card Zottelgarten

Business card is for a self-employed dog trainer with own dog school. Name and logo of the dog school are available. Color specifications as well. The design should be classy and minimalist, but also modern. An already existing idea would be: Front: Only the logo Back: Contact data

Font styles to use
Serif
Sans Serif
Other font styles liked:
• Trajan Pro

Colors
f78f20

Requirements
Must have
• Name: Margit Wendler-Rasch Title: Dipl. Dog Trainer Contain my logo Follow my font and color preferences (see files)

```html
<!DOCTYPE html>
<html lang="de">
<head>
<meta charset="utf-8">
<title>Zottelgarten – Visitenkarte</title>
<link href="https://fonts.googleapis.com/css2?family=Cinzel:wght@400&family=Work+Sans:wght@300;400&display=swap" rel="stylesheet">
<style>
  :root {
    --orange: #f7901f;
    --brown: #7b6a5d;
    --ink: #3a3430;
    --paper: #ffffff;
    --backdrop: #ece6df;
  }
  * { margin: 0; padding: 0; box-sizing: border-box; }
  html, body { width: 1200px; height: 930px; overflow: hidden; }
  body { background: var(--backdrop); position: relative; font-family: "Work Sans", sans-serif; }

  .card {
    position: absolute;
    width: 644px; height: 368px;
    border-radius: 22px;
    overflow: hidden;
    box-shadow: 0 6px 14px rgba(0,0,0,.18);
  }
  .card--contact { left: 278px; top: 76px; background: var(--paper); }
  .card--brand { left: 277px; top: 486px; background: var(--orange); }

  /* contact side */
  .brand-mark {
    position: absolute; left: 112px; top: 98px;
    width: 116px; height: 116px; border-radius: 50%;
    background: var(--brown);
  }
  .brand-name {
    position: absolute; left: 20px; width: 300px; top: 218px;
    text-align: center;
    font-family: "Cinzel", serif; font-weight: 400;
    font-size: 24px; letter-spacing: 1px; color: var(--brown);
  }
  .divider {
    position: absolute; left: 331px; top: 98px;
    width: 2px; height: 156px; background: var(--orange);
  }
  .details { position: absolute; left: 376px; top: 95px; color: var(--ink); }
  .details__name {
    font-family: "Cinzel", serif; font-weight: 400;
    font-size: 18px; color: var(--orange); line-height: 22px;
  }
  .details__title, .details__address, .details__contact li {
    font-size: 15px; font-weight: 300; line-height: 20px;
  }
  .details__address { margin-top: 12px; }
  .details__contact { list-style: none; margin-top: 8px; }
  .details__contact li { display: flex; align-items: center; gap: 9px; }
  .details__contact svg { width: 12px; height: 12px; flex: none; }

  .wave { position: absolute; left: 0; top: 0; width: 644px; height: 368px; }

  /* brand side */
  .brand-seal {
    position: absolute; left: 242px; top: 79px;
    width: 160px; height: 160px; border-radius: 50%;
    background: var(--paper);
    box-shadow: 0 0 0 3px var(--orange), 0 0 0 5px var(--paper);
  }
  .brand-name--large {
    position: absolute; left: 0; width: 644px; top: 252px;
    text-align: center;
    font-family: "Cinzel", serif; font-weight: 400;
    font-size: 34px; letter-spacing: 1px; color: var(--paper);
  }
</style>
</head>
<body>

<section class="card card--contact">
  <div class="brand-mark"></div>
  <div class="brand-name">ZOTTELGARTEN</div>
  <div class="divider"></div>

  <div class="details">
    <p class="details__name">MARGIT WENDLER-RASCH</p>
    <p class="details__title">Dipl. Dog Trainer</p>
    <p class="details__address">Lindenweg 17,<br>Birkenau</p>
    <ul class="details__contact">
      <li>
        <svg viewBox="0 0 12 12" fill="none" stroke="#7b6a5d" stroke-width="1.2"><path d="M3 1.5 L4.5 3.8 L3.6 4.8 C4.3 6.4 5.5 7.7 7.2 8.4 L8.2 7.5 L10.5 9 L9.5 10.7 C5.5 10.3 1.7 6.5 1.3 2.5 Z"/></svg>
        (044) 318-2290
      </li>
      <li>
        <svg viewBox="0 0 12 12" fill="none" stroke="#7b6a5d" stroke-width="1.2"><rect x="1" y="2.5" width="10" height="7"/><path d="M1 2.5 L6 6.5 L11 2.5"/></svg>
        info@zottelgarten.ch
      </li>
      <li>
        <svg viewBox="0 0 12 12" fill="none" stroke="#7b6a5d" stroke-width="1"><circle cx="6" cy="6" r="5"/><ellipse cx="6" cy="6" rx="2.2" ry="5"/><path d="M1 6 H11 M2 3.5 H10 M2 8.5 H10"/></svg>
        www.zottelgarten.ch
      </li>
    </ul>
  </div>

  <svg class="wave" viewBox="0 0 644 368" aria-hidden="true">
    <path d="M0 330 C60 352 150 356 300 337 S480 302 560 312 C600 320 630 337 644 348 L644 368 L0 368 Z" fill="#f7901f"/>
    <path d="M0 338 C60 360 150 364 300 345 S480 310 560 320 C600 328 630 345 644 356 L644 368 L0 368 Z" fill="#7b6a5d" stroke="#ffffff" stroke-width="2.5"/>
  </svg>
</section>

<section class="card card--brand">
  <div class="brand-seal"></div>
  <div class="brand-name--large">ZOTTELGARTEN</div>
</section>

</body>
</html>
```